Morvitel show guide

I need to design a one page 7x10 pdf that will be printed. It will include our logo and the following text:

#1 Disaster Mitigation Lead Platform

We generated over 60 million in
revenue last year fo our contractors.

Leads types:
-Water Damage
-Fire Damage
-Mold Remediation
-Biohazard
-Plumbing
-Carpet Cleaning

Exclusive leads
No monthly fees
Only pay for valid leads

Stop by booth 814 to get to your cut!

Target Market(s)

Home service contractors

Colors
9bcb3b
0255a3

Requirements
Must have
• our logo and text
Should not have
• any clutter

```html
<!DOCTYPE html>
<html lang="en">
<head>
<meta charset="utf-8">
<title>Morvitel Show Guide</title>
<link rel="stylesheet" href="https://fonts.googleapis.com/css2?family=Fira+Sans+Condensed:wght@600;700;800;900&display=swap">
<style>
  :root {
    --lime: #9bcb3b;
    --navy: #0255a3;
    --leaf: #16a04a;
    --tick: #4a78c0;
    --ink: #111111;
    --white: #ffffff;
  }
  * { margin: 0; padding: 0; box-sizing: border-box; }
  html, body { width: 840px; height: 1200px; overflow: hidden; }
  body {
    position: relative;
    background: var(--lime);
    font-family: "Fira Sans Condensed", "Arial Narrow", sans-serif;
    font-weight: 700;
  }
  .abs { position: absolute; }

  .rank-badge {
    left: 216px; top: 22px; width: 380px; height: 380px;
    border-radius: 50%;
    background: var(--white);
    border: 28px solid var(--navy);
  }
  .rank-number {
    left: 0; width: 780px; top: 74px;
    text-align: center;
    font-size: 200px; font-weight: 900; line-height: 1;
    color: var(--navy);
    text-shadow: 2px 3px 3px rgba(0,0,0,0.35);
  }
  .title-banner { left: 118px; top: 273px; }
  .title-text {
    left: 118px; width: 588px; top: 287px;
    text-align: center;
    color: var(--white);
    font-size: 66px; line-height: 70px;
    white-space: nowrap;
    text-shadow: 2px 2px 3px rgba(0,0,0,0.35);
  }

  .revenue-pill {
    left: 68px; top: 470px; width: 702px; height: 106px;
    background: var(--white);
    border-radius: 50px;
  }
  .revenue-text {
    left: 108px; top: 474px;
    color: var(--leaf);
    font-size: 42.5px; line-height: 47px;
    white-space: nowrap;
  }
  .revenue-figure {
    color: var(--tick);
    font-size: 52px;
    line-height: 1;
    text-decoration: underline;
    text-decoration-thickness: 3px;
    text-underline-offset: 3px;
  }

  .info-panel {
    left: 42px; top: 592px; width: 756px; height: 700px;
    background: var(--white);
    border-radius: 56px;
  }
  .section-label {
    left: 141px; top: 622px; width: 246px; height: 52px;
    background: var(--navy);
    color: var(--white);
    font-size: 37px; line-height: 52px;
    text-align: center;
  }
  .lead-list { left: 94px; top: 694px; list-style: none; }
  .lead-list li {
    display: flex; align-items: center;
    height: 50px;
    font-size: 36px; color: var(--ink);
  }
  .lead-list svg { width: 36px; height: 32px; margin-right: 18px; }

  .perk {
    right: 86px; height: 45px;
    background: var(--leaf);
    color: var(--white);
    font-size: 33.5px; line-height: 45px;
    text-align: center;
    white-space: nowrap;
  }
  .perk-exclusive { top: 704px; width: 248px; }
  .perk-fees { top: 796px; width: 251px; }
  .perk-valid { top: 884px; width: 349px; }

  .booth-pill {
    left: 94px; top: 1032px; width: 664px; height: 74px;
    background: var(--navy);
    border-radius: 37px;
    color: var(--white);
    font-size: 41px; line-height: 74px;
    text-align: center;
    white-space: nowrap;
    text-shadow: 2px 2px 3px rgba(0,0,0,0.35);
  }

  .brand-name {
    left: 0; width: 840px; top: 1136px;
    text-align: center;
    color: var(--navy);
    font-size: 34px; font-weight: 700; line-height: 44px;
  }
</style>
</head>
<body>
  <div class="abs rank-badge"></div>
  <div class="abs rank-number">#1</div>

  <svg class="abs title-banner" width="588" height="166" viewBox="0 0 588 166" aria-hidden="true">
    <path d="M0 0 H588 V166 H55 V107 H0 Z" fill="#0255a3"/>
  </svg>
  <h1 class="abs title-text">Disaster Mitigation<br>Lead Platform</h1>

  <div class="abs revenue-pill"></div>
  <p class="abs revenue-text">We generated over <span class="revenue-figure">60</span> million in<br>revenue last year for our contractors</p>

  <div class="abs info-panel"></div>
  <h2 class="abs section-label">LEADS TYPES</h2>

  <ul class="abs lead-list">
    <li><svg viewBox="0 0 36 32"><path d="M2 18 L12 28 L34 3 L13 20 Z" fill="#4a78c0"/></svg>Water Damage</li>
    <li><svg viewBox="0 0 36 32"><path d="M2 18 L12 28 L34 3 L13 20 Z" fill="#4a78c0"/></svg>Fire Damage</li>
    <li><svg viewBox="0 0 36 32"><path d="M2 18 L12 28 L34 3 L13 20 Z" fill="#4a78c0"/></svg>Mold Remediation</li>
    <li><svg viewBox="0 0 36 32"><path d="M2 18 L12 28 L34 3 L13 20 Z" fill="#4a78c0"/></svg>Biohazard</li>
    <li><svg viewBox="0 0 36 32"><path d="M2 18 L12 28 L34 3 L13 20 Z" fill="#4a78c0"/></svg>Plumbing</li>
    <li><svg viewBox="0 0 36 32"><path d="M2 18 L12 28 L34 3 L13 20 Z" fill="#4a78c0"/></svg>Carpet Cleaning</li>
  </ul>

  <div class="abs perk perk-exclusive">Exclusive leads</div>
  <div class="abs perk perk-fees">No monthly fees</div>
  <div class="abs perk perk-valid">Only pay for valid leads</div>

  <div class="abs booth-pill">Stop by booth 814 to get to your cut!</div>

  <div class="abs brand-name">Quillmarsh</div>
</body>
</html>
```